3 Politically Incorrect Greeting Cards

I would like to see some clean, colorful, and modern designs for 3 "politically incorrect" greeting cards aimed at young, single, successful women. I would like them to say:

Card 1: " Congratulations on not marrying the wrong person"
Card 2: " Congratulations on buying a house without a husband"
Card 3: " Thank you for not forgetting about me now that you have a boyfriend"

My initial thought was to have a white background with simple black writing, but I think a colorful background with a white text box in the middle might be more appropriate. I can't imagine the cards having any images/icons on them, but I'm open to suggestions if you think it would improve on the design. You guys are likely more creative than I am.

I've included a couple pics of looks I like - but like I said - I'm open to suggestions and what I like may not be appropriate for these cards. All the cards can have a similar esthetic or theme (maybe the same fonts but different colors or different color florals in each) or they can be completely different.

Target Market(s)

Young, single, successful women mid-20s to mid 40's.

Font styles to use
Serif
Sans Serif
Other font styles liked:
• Watercolour lettering maybe

Colors

Designer to choose colors to be used in the design.

Requirements
Must have
• Clean, colorful, bright, professional looking. The right tone for the message.
• I think the message is bold so the writing and colors have to be as well. I have included examples of ideas I like.
Nice to have
• Images, illustrations, icons, maybe patterns or some decorative details. Something to make the card more interesting than just the words (like the blue background with black letters one I made). I like a bright pattern with a white box in the center with the text.
Should not have
• Special effects, galaxy pictures, ugly images, bland colors.

```html
<!DOCTYPE html>
<html lang="en">
<head>
<meta charset="utf-8">
<title>Greeting Card Set</title>
<link rel="stylesheet" href="https://fonts.googleapis.com/css2?family=Satisfy&display=swap">
<style>
  :root {
    --backdrop: #ecebea;
    --card-white: #ffffff;
    --text-white: #ffffff;
    --pink: #d772ad;
    --magenta: #c46bb2;
    --lilac: #b58fd0;
    --blush: #efa9c8;
    --sky: #6ec3e6;
    --aqua: #52bfd0;
    --mint: #8fd3b6;
    --seafoam: #a6dccd;
    --amber: #efb36e;
    --honey: #f2cf7d;
    --peach: #f4c49a;
    --cream: #fdf4e6;
    --shadow: rgba(40, 30, 20, 0.28);
  }
  * { margin: 0; padding: 0; box-sizing: border-box; }
  html, body {
    width: 1200px;
    height: 603px;
    overflow: hidden;
    background: var(--backdrop);
  }
  .card-set {
    position: relative;
    width: 1200px;
    height: 603px;
  }
  .card {
    position: absolute;
    top: 74px;
    width: 317px;
    height: 444px;
    background: var(--card-white);
    box-shadow: 3px 4px 8px var(--shadow);
    overflow: hidden;
  }
  .card--wrong-person { left: 80px; }
  .card--new-house { left: 449px; }
  .card--boyfriend { left: 818px; }

  .card__wash {
    position: absolute;
    inset: 0;
  }
  .card--wrong-person .card__wash {
    background:
      radial-gradient(ellipse 60% 30% at 30% 22%, rgba(181,143,208,0.75), transparent 70%),
      radial-gradient(ellipse 70% 28% at 75% 38%, rgba(215,114,173,0.9), transparent 75%),
      radial-gradient(ellipse 80% 32% at 40% 62%, rgba(196,107,178,0.85), transparent 75%),
      radial-gradient(ellipse 70% 22% at 60% 82%, rgba(181,143,208,0.55), transparent 75%),
      linear-gradient(180deg, var(--card-white) 8%, var(--blush) 28%, var(--pink) 50%, var(--magenta) 68%, var(--lilac) 82%, var(--card-white) 96%);
  }
  .card--new-house .card__wash {
    background:
      radial-gradient(ellipse 60% 25% at 25% 10%, rgba(143,211,182,0.8), transparent 75%),
      radial-gradient(ellipse 70% 30% at 70% 35%, rgba(82,191,208,0.85), transparent 75%),
      radial-gradient(ellipse 70% 30% at 35% 65%, rgba(110,195,230,0.8), transparent 75%),
      radial-gradient(ellipse 70% 25% at 65% 85%, rgba(143,211,182,0.85), transparent 75%),
      linear-gradient(180deg, var(--seafoam) 0%, var(--sky) 30%, var(--aqua) 55%, var(--mint) 80%, var(--card-white) 100%);
  }
  .card--boyfriend .card__wash {
    background:
      radial-gradient(ellipse 60% 25% at 60% 8%, rgba(242,207,125,0.9), transparent 75%),
      radial-gradient(ellipse 80% 30% at 40% 45%, rgba(239,179,110,0.7), transparent 75%),
      linear-gradient(180deg, var(--honey) 0%, var(--amber) 25%, var(--amber) 45%, var(--peach) 62%, var(--cream) 80%, var(--card-white) 100%);
  }

  .card__message {
    position: absolute;
    left: 0;
    right: 0;
    font-family: "Satisfy", cursive;
    font-size: 33px;
    line-height: 49px;
    color: var(--text-white);
    text-align: center;
  }
  .card--wrong-person .card__message { top: 134px; }
  .card--new-house .card__message { top: 134px; }
  .card--boyfriend .card__message { top: 102px; }

  .card__emphasis {
    text-decoration: underline;
    text-decoration-thickness: 2px;
    text-underline-offset: 6px;
  }
</style>
</head>
<body>
  <main class="card-set">
    <article class="card card--wrong-person">
      <div class="card__wash" role="img" aria-label="Pink and purple watercolour wash"></div>
      <p class="card__message">Congratulations on<br><span class="card__emphasis">not</span> marrying the<br>wrong person</p>
    </article>
    <article class="card card--new-house">
      <div class="card__wash" role="img" aria-label="Blue and green watercolour wash"></div>
      <p class="card__message">Congratulations on<br>buying a house<br>without a husband</p>
    </article>
    <article class="card card--boyfriend">
      <div class="card__wash" role="img" aria-label="Golden orange watercolour wash"></div>
      <p class="card__message">Thank you for <span class="card__emphasis">not</span><br>forgetting about me<br>now that you<br>have a boyfriend</p>
    </article>
  </main>
</body>
</html>
```